Nerov Modellwerk.Brenn GmbH needed a letterhead template

For English scroll down. We need a letterhead template and since we already have our logo design successfully with you, we now want to also design the letterhead with you. Down in the uploaded file you see what is important and what should definitely be seen on our template. The template should be like the homepage (www.modellwerk.brenn) held in red, blue and white. We need a letter-head submission. In the bottom in the chapter "databases uploading" you can find the most important things, did must be on the submission. The submission shoulderstand be in the colors blue, red and white like our homepage (www.modellwerk.brenn).

```html
<!DOCTYPE html>
<html lang="de">
<head>
<meta charset="utf-8">
<title>Nerov Modellwerk.Brenn GmbH – Briefpapier</title>
<link rel="stylesheet" href="https://fonts.googleapis.com/css2?family=Open+Sans:wght@700&display=swap">
<style>
  :root {
    --backdrop: #d0d0d1;
    --paper: #f1f2f2;
    --brand-blue: #1559a8;
    --brand-red: #c8202b;
    --watermark: #e4e7ec;
    --white: #ffffff;
  }
  * { margin: 0; padding: 0; box-sizing: border-box; }
  html, body {
    width: 1200px;
    height: 1000px;
    overflow: hidden;
    background: var(--backdrop);
    font-family: "Open Sans", Arial, sans-serif;
    font-weight: 700;
  }
  .letterhead {
    position: absolute;
    left: 315px;
    top: 100px;
    width: 590px;
    height: 835px;
    background: var(--paper);
    box-shadow: 0 4px 18px rgba(0,0,0,0.18);
  }
  .brand {
    position: absolute;
    left: 22px;
    top: 42px;
    display: flex;
    align-items: center;
    gap: 8px;
  }
  .brand-dot {
    width: 14px;
    height: 14px;
    border-radius: 50%;
    background: var(--brand-blue);
  }
  .brand-name {
    color: var(--brand-blue);
    font-size: 22px;
    letter-spacing: -0.2px;
  }
  .sender {
    position: absolute;
    left: 430px;
    top: 35px;
    color: var(--brand-blue);
    font-size: 9.5px;
    line-height: 13px;
    font-style: normal;
    white-space: nowrap;
  }
  .watermark {
    position: absolute;
    left: 175px;
    top: 330px;
    width: 230px;
    height: 190px;
    border-radius: 50%;
    background: var(--watermark);
    opacity: 0.55;
  }
  .footer-rule {
    position: absolute;
    left: 0;
    top: 758px;
    width: 100%;
    height: 8px;
    border-top: 3px solid var(--brand-red);
    border-bottom: 3px solid var(--brand-blue);
  }
  .footer {
    position: absolute;
    left: 0;
    top: 768px;
    width: 100%;
    height: 67px;
    background: var(--brand-blue);
    color: var(--white);
    font-size: 9.5px;
    line-height: 12.5px;
    white-space: nowrap;
  }
  .footer-col { position: absolute; top: 6px; font-style: normal; }
  .footer-col.company { left: 21px; }
  .footer-col.contact { left: 239px; }
  .footer-col.bank { left: 434px; }
</style>
</head>
<body>
  <main class="letterhead">
    <header>
      <div class="brand">
        <span class="brand-dot"></span>
        <span class="brand-name">Modellwerk.Brenn</span>
      </div>
      <address class="sender">
        Nerov Modellwerk.Brenn GmbH<br>
        Auenweg 12<br>
        6199 Brennbach, Tirol<br>
        Österreich
      </address>
    </header>

    <div class="watermark" aria-hidden="true"></div>

    <div class="footer-rule"></div>
    <footer class="footer">
      <address class="footer-col company">
        Geschäftsführer Dr. Marten Lukas<br>
        Auenweg 12<br>
        6199 Brennbach, Tirol<br>
        Österreich
      </address>
      <div class="footer-col contact">
        Telefon: 0800 XX XX XX<br>
        Mail: contact@modellwerk.brenn<br>
        Web: www.modellwerk.brenn
      </div>
      <div class="footer-col bank">
        Talbank XXXX<br>
        IBAN: ATXX XXXX XXXX XXXX<br>
        BIC: XXXX<br>
        UID - Nr .: ATUXXXXX
      </div>
    </footer>
  </main>
</body>
</html>
```